Spinning Wheel: Spin & Win

We are looking to design a large sticker cover for a spinning wheel (please see attached reference)

Wheel diameter: 120 cm (1.2meters)

Divided into 8 sections:
1- Free Meal
2- Tolvik Gift Card
3- Haircut or Blowdry
4- Tolvik Gift Card
5- Merchandise
6- Tolvik Gift Card
7- Meal voucher
8- Tolvik Gift Card

Text in the center:
Buy for 200 AED to Spin & Win!
(Spin & Win should be the most dominant visually)

Font: Something classy and elegant (maybe cursive but easily read)

Colors: Khaki - All shades of brown and dark brown (note: the wheel structure is made of wood that is dark brown)

Feel: Wood and Old Paper
Updates

Target Market(s)

Upper Class

Industry/Entity Type

Graphic Design

Font styles to use
Decorative
Script

Requirements
Should not have
• Flashy colors

```html
<!DOCTYPE html>
<html lang="en">
<head>
<meta charset="utf-8">
<title>Spin &amp; Win Wheel</title>
<link rel="stylesheet" href="https://fonts.googleapis.com/css2?family=Pinyon+Script&display=swap">
<style>
  :root {
    --page: #ffffff;
    --wood-dark: #3a1a0c;
    --wood-mid: #6b2f14;
    --wood-warm: #8a4420;
    --divider: #d9935a;
    --rim: #c77a45;
    --label: #f0b48a;
    --hub-light: #e8c79a;
    --hub-mid: #c9995f;
    --hub-edge: #8f5e2e;
    --ink: #1e130c;
  }
  html, body {
    margin: 0;
    padding: 0;
    width: 1200px;
    height: 1200px;
    overflow: hidden;
    background: var(--page);
  }
  .wheel {
    display: block;
    width: 1200px;
    height: 1200px;
  }
  .prize-label {
    font-family: "Pinyon Script", cursive;
    font-size: 46px;
    fill: var(--label);
  }
  .hub-intro {
    font-family: "Pinyon Script", cursive;
    font-size: 30px;
    fill: var(--ink);
  }
  .hub-headline {
    font-family: "Pinyon Script", cursive;
    font-size: 150px;
    fill: var(--ink);
  }
  .hub-amp {
    font-family: "Pinyon Script", cursive;
    font-size: 60px;
    fill: var(--ink);
  }
</style>
</head>
<body>
<svg class="wheel" viewBox="0 0 1200 1200" xmlns="http://www.w3.org/2000/svg">
  <defs>
    <radialGradient id="woodFace" cx="600" cy="600" r="600" gradientUnits="userSpaceOnUse">
      <stop offset="0.3" stop-color="var(--wood-warm)"/>
      <stop offset="0.7" stop-color="var(--wood-mid)"/>
      <stop offset="1" stop-color="var(--wood-dark)"/>
    </radialGradient>
    <radialGradient id="hubFace" cx="560" cy="560" r="260" gradientUnits="userSpaceOnUse">
      <stop offset="0" stop-color="var(--hub-light)"/>
      <stop offset="0.7" stop-color="var(--hub-mid)"/>
      <stop offset="1" stop-color="var(--hub-edge)"/>
    </radialGradient>
  </defs>

  <!-- wheel face -->
  <circle class="wheel-face" cx="600" cy="600" r="596" fill="url(#woodFace)"/>
  <circle class="wheel-rim" cx="600" cy="600" r="592" fill="none" stroke="var(--rim)" stroke-width="7"/>

  <!-- section dividers -->
  <g class="dividers" stroke="var(--divider)" stroke-width="7" stroke-linecap="round">
    <line x1="600" y1="372" x2="600" y2="8"/>
    <line x1="600" y1="828" x2="600" y2="1192"/>
    <line x1="372" y1="600" x2="8" y2="600"/>
    <line x1="828" y1="600" x2="1192" y2="600"/>
    <line x1="761" y1="439" x2="1019" y2="181"/>
    <line x1="439" y1="761" x2="181" y2="1019"/>
    <line x1="439" y1="439" x2="181" y2="181"/>
    <line x1="761" y1="761" x2="1019" y2="1019"/>
  </g>

  <!-- prize labels -->
  <g class="prize-labels" text-anchor="middle">
    <text class="prize-label" transform="translate(600 600) rotate(-67.5) translate(430 14)">Free Meal</text>
    <text class="prize-label" transform="translate(600 600) rotate(-22.5) translate(430 14)">Tolvik Gift Card</text>
    <text class="prize-label" transform="translate(600 600) rotate(22.5) translate(430 14)">Haircut or Blowdry</text>
    <text class="prize-label" transform="translate(600 600) rotate(67.5) translate(430 14)">Tolvik Gift Card</text>
    <text class="prize-label" transform="translate(600 600) rotate(-67.5) translate(-430 14)">Merchandise</text>
    <text class="prize-label" transform="translate(600 600) rotate(157.5) translate(430 14)">Tolvik Gift Card</text>
    <text class="prize-label" transform="translate(600 600) rotate(202.5) translate(430 14)">Meal voucher</text>
    <text class="prize-label" transform="translate(600 600) rotate(247.5) translate(430 14)">Tolvik Gift Card</text>
  </g>

  <!-- centre hub -->
  <circle class="hub" cx="600" cy="600" r="230" fill="url(#hubFace)" stroke="var(--wood-dark)" stroke-width="4"/>
  <g class="hub-copy">
    <text class="hub-intro" x="600" y="442" text-anchor="middle">Buy for 200 AED to</text>
    <text class="hub-headline" x="510" y="570" text-anchor="middle">Spin</text>
    <text class="hub-amp" x="520" y="625" text-anchor="middle">&amp;</text>
    <text class="hub-headline" x="630" y="750" text-anchor="middle">Win!</text>
  </g>
</svg>
</body>
</html>
```